Visitenkarten-Design für K17.eu - TradeWing Finanz
Zielgruppe
Smartphone-Banking mit Mehrwert
Aufgabenstellung
Bitte entwerfen Sie kreative Visitenkarten für uns.
- Halten Sie einen Platz/Rahmen frei für Fotos, die wir nachträglich einsetzen, und kennzeichnen diesen.
- Halten Sie einen Patz/Rahmen für Vor- und Nachname sowie für die Berufsbezeichnung frei und kennzeichnen diesen.
- Halten Sie einen Platz/Rahmen für die Telefonnummern und die Email-Adressen frei und kennzeichnen diesen.
Alle Visitenkarten sollen folgende Daten beinhalten:
Vorname Nachname*
Berufsbezeichnung*
Mobile:
Office:
Email:
Domain:
* = individuell, jeder Mitarbeiter hat eigene Daten
Die Farben müssen sich an unserem CI-Design orientieren, orange/weiß/schwarz/grau -
Außerdem finden Sie unser Logo in der Anlage, welches Sie bitte auf der Karte platzieren.
Bitte liefern Sie uns die Designs in verschiedenen Formaten - psd, ai, eps, jpg, png
Bei Fragen zögern Sie nicht, uns zu kontaktieren. Danke.

```html
<!DOCTYPE html>
<html lang="de">
<head>
<meta charset="utf-8">
<title>K17.eu – Visitenkarte</title>
<link rel="stylesheet" href="https://fonts.googleapis.com/css2?family=Arimo:wght@400;700&display=swap">
<style>
  :root {
    --bg: #dcdcdc;
    --paper: #ffffff;
    --orange: #d9762e;
    --orange-back: #dc8540;
    --grey: #5a5a5a;
    --grey-dark: #4a4a4a;
    --ink: #1b1b1b;
  }
  * { margin: 0; padding: 0; box-sizing: border-box; }
  html, body { width: 1200px; height: 873px; overflow: hidden; }
  body {
    background: var(--bg);
    font-family: "Arimo", Arial, sans-serif;
    position: relative;
  }
  .card {
    position: absolute;
    top: 268px;
    width: 520px;
    height: 336px;
    overflow: hidden;
    box-shadow: 0 6px 18px rgba(0,0,0,.18);
  }
  .card--front { left: 60px; background: var(--paper); }
  .card--back { left: 620px; background: var(--orange-back); }

  /* front */
  .front-band {
    position: absolute; left: 0; right: 0; bottom: 0;
    height: 30px; background: var(--orange);
  }
  .brand {
    position: absolute; left: 30px; top: 26px;
    display: flex; align-items: center; gap: 8px;
  }
  .brand__mark { width: 14px; height: 14px; background: var(--orange); }
  .brand__name {
    font-weight: 700; font-size: 28px; color: var(--orange); letter-spacing: .5px;
  }
  .brand__domain {
    position: absolute; left: 30px; top: 62px;
    font-weight: 700; font-size: 12px; color: var(--grey-dark);
  }
  .phone-frame {
    position: absolute; left: 30px; top: 160px;
    width: 214px; height: 130px;
    background: var(--ink); border-radius: 16px;
    padding: 10px 30px 10px 30px;
  }
  .phone-frame::before {
    content: ""; position: absolute; left: 11px; top: 57px;
    width: 12px; height: 12px; border: 1.5px solid #555; border-radius: 50%;
  }
  .photo-slot {
    width: 100%; height: 100%;
    background: radial-gradient(ellipse at 50% 45%, #b07c5d 0%, #8a5c44 40%, #5a4034 100%);
  }
  .details { position: absolute; left: 290px; top: 70px; color: var(--grey); }
  .address { font-size: 13px; line-height: 17px; }
  .person { margin-top: 28px; }
  .person__name { font-size: 17px; color: var(--orange); }
  .person__role { font-size: 13px; margin-top: 3px; }
  .contact {
    position: absolute; left: 250px; top: 218px;
    display: grid; grid-template-columns: 34px auto; row-gap: 4px;
    font-size: 13px; line-height: 17px; color: var(--grey);
  }
  .contact svg { display: block; }

  /* back */
  .back-logo {
    position: absolute; left: 0; right: 0; top: 110px;
    display: flex; justify-content: center; align-items: center; gap: 14px;
  }
  .back-logo__mark { width: 30px; height: 30px; background: #ffffff; }
  .back-logo__name { font-weight: 700; font-size: 72px; color: #ffffff; }
  .back-domain {
    position: absolute; left: 0; right: 0; top: 210px; text-align: center;
    font-weight: 700; font-size: 26px; color: var(--grey-dark);
  }
</style>
</head>
<body>
  <section class="card card--front" aria-label="Vorderseite">
    <div class="brand"><span class="brand__mark"></span><span class="brand__name">K17.eu</span></div>
    <div class="brand__domain">www.k17.eu</div>

    <div class="details">
      <p class="address">Ahornstr. 9<br>94036 Talheim<br>Germany</p>
      <div class="person">
        <p class="person__name">Vorname Nachname</p>
        <p class="person__role">Berufsbezeichnung</p>
      </div>
    </div>

    <div class="contact">
      <svg width="24" height="30" viewBox="0 0 24 30" aria-hidden="true">
        <rect x="3" y="1" width="18" height="28" rx="3" fill="none" stroke="#d9762e" stroke-width="1.6"/>
        <line x1="3" y1="6" x2="21" y2="6" stroke="#d9762e" stroke-width="1.2"/>
        <line x1="3" y1="24" x2="21" y2="24" stroke="#d9762e" stroke-width="1.2"/>
      </svg>
      <span>+49 170 xxxxxxx<br>+49 800 xxxxxx-xx</span>
      <svg width="24" height="18" viewBox="0 0 24 18" aria-hidden="true">
        <rect x="1" y="1" width="22" height="16" fill="none" stroke="#d9762e" stroke-width="1.6"/>
        <polyline points="1,1 12,10 23,1" fill="none" stroke="#d9762e" stroke-width="1.4"/>
        <line x1="1" y1="17" x2="10" y2="8" stroke="#d9762e" stroke-width="1.2"/>
        <line x1="23" y1="17" x2="14" y2="8" stroke="#d9762e" stroke-width="1.2"/>
      </svg>
      <span>vorname@k17.eu</span>
    </div>

    <div class="phone-frame">
      <div class="photo-slot" role="img" aria-label="Platz für das Foto des Mitarbeiters"></div>
    </div>

    <div class="front-band"></div>
  </section>

  <section class="card card--back" aria-label="Rückseite">
    <div class="back-logo"><span class="back-logo__mark"></span><span class="back-logo__name">K17.eu</span></div>
    <div class="back-domain">www.k17.eu</div>
  </section>
</body>
</html>
```